4 x Designs Required

Hi There,
I require 4 x different designs to be made for 4 new brands of mine however they can be quite interchangeable. HR Brevlo and Marketing Brevlo can be similar just with a difference in colour. The same goes for the Bulletin brands. This means there are ultimately two designs that need perfecting.

There must be a click here CTA on the banner somewhere. :-)

I require the banners in 728x90 format and 960x90 please.

Please use strap lines on the banners such as:
Essential Whitepapers for HR Professionals
Essential Whitepapers for Marketing Professionals
Your No.1 Whitepaper Resource

The brand names:
HR Brevlo
Marketing Brevlo
HR Gazettor
Marketing Gazettor

Examples attached.

```html
<!DOCTYPE html>
<html lang="en">
<head>
<meta charset="utf-8">
<title>4 x Designs Required – 960x90 Banners</title>
<link rel="stylesheet" href="https://fonts.googleapis.com/css2?family=Catamaran:wght@500;600&family=Montserrat:wght@300;400;500;600;700;800&display=swap">
<style>
  :root {
    --page: #ffffff;
    --ink: #1a1a1a;
    --white: #ffffff;
    --red: #e32a3b;
    --plum: #4a1f45;
    --navy: #0c2f5c;
    --blue: #0a5c98;
    --maroon-dark: #220b0d;
    --maroon: #561b1c;
    --yellow: #e8ad16;
    --cta-ink: #1d2440;
    --amber: #b4600f;
    --rust: #7a2c18;
    --midnight: #0c0c24;
    --orange: #f3a214;
    --deep-sea: #03131d;
    --teal: #0f4456;
    --cyan: #12b1ec;
  }
  * { box-sizing: border-box; margin: 0; padding: 0; }
  html, body {
    width: 1200px; height: 772px; overflow: hidden;
    background: var(--page);
  }
  .sheet { position: relative; width: 1200px; height: 772px; }
  .sheet-title {
    position: absolute; top: 50px; left: 0; width: 1200px;
    text-align: center;
    font: 400 23px/28px "Montserrat", sans-serif;
    letter-spacing: 1.2px; color: var(--ink);
  }
  .banner {
    position: absolute; left: 61px; width: 1071px; height: 101px;
    overflow: hidden; color: var(--white);
  }
  .banner svg.deco { position: absolute; inset: 0; }
  .brand, .tagline, .cta, .rule { position: absolute; white-space: nowrap; }

  /* HR Brevlo */
  .banner--hr-brevlo {
    top: 109px;
    background: linear-gradient(90deg, var(--red) 0%, #a41c3c 28%, var(--plum) 40%, var(--navy) 58%, var(--blue) 85%);
  }
  .banner--hr-brevlo .brand {
    left: 27px; top: 0; height: 101px; display: flex; align-items: center;
    font: 300 50px/1 "Montserrat", sans-serif; letter-spacing: -1.5px;
  }
  .banner--hr-brevlo .brand strong { font-weight: 800; margin-left: 12px; }
  .banner--hr-brevlo .tagline {
    left: 366px; top: 0; height: 101px; display: flex; align-items: center;
    font: 500 27px/1 "Catamaran", sans-serif;
  }
  .banner--hr-brevlo .cta {
    right: 18px; top: 0; height: 101px; display: flex; flex-direction: column; justify-content: center;
    font: 700 27px/29px "Montserrat", sans-serif;
  }

  /* Marketing Brevlo */
  .banner--marketing-brevlo {
    top: 282px;
    background: radial-gradient(ellipse at 40% 110%, #5c1d1d 0%, transparent 55%),
                linear-gradient(90deg, var(--maroon-dark) 0%, #2c0f10 40%, var(--maroon) 100%);
  }
  .stacked-brand { left: 32px; top: 15px; }
  .stacked-brand .brand-top { display: block; font: 400 31px/33px "Montserrat", sans-serif; letter-spacing: 0.5px; }
  .stacked-brand .brand-main { display: block; font: 800 42px/42px "Montserrat", sans-serif; letter-spacing: -0.5px; }
  .banner--marketing-brevlo .brand-main { color: var(--yellow); }
  .banner--marketing-brevlo .rule { left: 279px; width: 553px; height: 1px; background: var(--white); opacity: 0.85; }
  .banner--marketing-brevlo .rule--top { top: 24px; }
  .banner--marketing-brevlo .rule--bottom { top: 76px; }
  .banner--marketing-brevlo .tagline {
    left: 281px; width: 551px; top: 0; height: 101px; display: flex; align-items: center;
    font: 500 26px/1 "Catamaran", sans-serif; color: var(--yellow);
  }
  .tagline .hl { color: var(--white); }
  .banner--marketing-brevlo .cta {
    left: 898px; top: 31px; width: 146px; height: 38px;
    background: var(--yellow); border-radius: 5px;
    display: flex; align-items: center; justify-content: center;
    font: 600 18px/1 "Montserrat", sans-serif; color: var(--cta-ink);
  }

  /* HR Gazettor */
  .banner--hr-gazettor {
    top: 454px;
    background: linear-gradient(100deg, var(--amber) 0%, var(--rust) 32%, #4a2a2a 55%, #2c1d33 75%, var(--midnight) 100%);
  }
  .banner--hr-gazettor .glow {
    position: absolute; left: 440px; top: -30px; width: 420px; height: 160px;
    background: radial-gradient(ellipse at center, rgba(230,170,130,0.22), transparent 65%);
  }
  .banner--hr-gazettor .brand {
    left: 36px; top: 0; height: 101px; display: flex; align-items: center;
    font: 300 48px/1 "Montserrat", sans-serif; letter-spacing: -2px;
  }
  .banner--hr-gazettor .brand strong { font-weight: 800; margin-left: 12px; }
  .banner--hr-gazettor .tagline { left: 503px; top: 19px; width: 300px; text-align: center; font-family: "Montserrat", sans-serif; }
  .banner--hr-gazettor .tagline-lead { display: block; font-weight: 400; font-size: 40px; line-height: 38px; color: var(--orange); }
  .banner--hr-gazettor .tagline-sub { display: block; font-weight: 500; font-size: 22px; line-height: 26px; }
  .banner--hr-gazettor .cta {
    left: 846px; top: 0; height: 101px; display: flex; align-items: center; gap: 13px;
    font: 700 29px/1 "Montserrat", sans-serif; color: var(--orange);
  }

  /* Marketing Gazettor */
  .banner--marketing-gazettor {
    top: 626px;
    background: radial-gradient(ellipse at 55% 30%, rgba(20,70,90,0.35), transparent 60%),
                linear-gradient(90deg, var(--deep-sea) 0%, #041826 50%, var(--teal) 100%);
  }
  .banner--marketing-gazettor .stacked-brand { left: 30px; top: 15px; }
  .banner--marketing-gazettor .brand-main { color: var(--cyan); font-size: 42px; line-height: 44px; }
  .banner--marketing-gazettor .tagline {
    left: 326px; top: 0; height: 101px; display: flex; align-items: center;
    font: 500 26px/1 "Catamaran", sans-serif; color: var(--cyan);
  }
  .banner--marketing-gazettor .cta {
    left: 939px; top: 8px; width: 86px; height: 86px; border-radius: 50%;
    background: var(--cyan);
    display: flex; flex-direction: column; align-items: center; justify-content: center;
    font: 800 19px/19px "Montserrat", sans-serif;
  }
</style>
</head>
<body>
<main class="sheet">
  <h1 class="sheet-title">4 X DESIGNS REQUIRED_960X90</h1>

  <section class="banner banner--hr-brevlo">
    <svg class="deco" width="1071" height="101" viewBox="0 0 1071 101">
      <polygon points="290,0 320,0 355,50 320,101 290,101 325,50" fill="#ffffff" opacity="0.06"/>
      <polygon points="320,0 345,0 380,50 345,101 320,101 355,50" fill="#000000" opacity="0.08"/>
      <polygon points="880,0 905,0 870,50 905,101 880,101 845,50" fill="#1a8ad0" opacity="0.35"/>
      <polygon points="905,0 935,0 900,50 935,101 905,101 870,50" fill="#0a4a80" opacity="0.5"/>
      <polygon points="935,0 962,0 926,50 962,101 935,101 900,50" fill="#1a8ad0" opacity="0.4"/>
      <defs>
        <linearGradient id="gold" x1="0" y1="0" x2="0" y2="1">
          <stop offset="0" stop-color="#d8aa1c"/>
          <stop offset="1" stop-color="#a67a00"/>
        </linearGradient>
      </defs>
      <polygon points="962,0 1071,0 1071,101 962,101 926,50" fill="url(#gold)"/>
    </svg>
    <div class="brand">HR<strong>BREVLO</strong></div>
    <p class="tagline">Essential Whitepapers for HR Professionals</p>
    <div class="cta"><span>CLICK</span><span>HERE</span></div>
  </section>

  <section class="banner banner--marketing-brevlo">
    <div class="brand stacked-brand">
      <span class="brand-top">MARKETING</span>
      <span class="brand-main">BREVLO</span>
    </div>
    <span class="rule rule--top"></span>
    <p class="tagline">Essential&nbsp;<span class="hl">Whitepapers</span>&nbsp;for Marketing Professionals</p>
    <span class="rule rule--bottom"></span>
    <div class="cta">CLICK HERE</div>
  </section>

  <section class="banner banner--hr-gazettor">
    <div class="glow" role="img" aria-label="Soft bokeh light background"></div>
    <svg class="deco" width="1071" height="101" viewBox="0 0 1071 101">
      <polygon points="848,0 1071,0 1071,101 779,101" fill="#0c0c24" opacity="0.85"/>
    </svg>
    <div class="brand">HR<strong>GAZETTOR</strong></div>
    <p class="tagline">
      <span class="tagline-lead">YOUR NO.1</span>
      <span class="tagline-sub">WHITEPAPER RESOURCE</span>
    </p>
    <div class="cta">
      <svg width="13" height="15" viewBox="0 0 13 15"><polygon points="0,0 13,7.5 0,15" fill="#ffffff"/></svg>
      <span>CLICK HERE</span>
    </div>
  </section>

  <section class="banner banner--marketing-gazettor">
    <svg class="deco" width="1071" height="101" viewBox="0 0 1071 101">
      <circle cx="982" cy="51" r="74" fill="#061a33" opacity="0.55"/>
      <circle cx="982" cy="51" r="60" fill="#04142a" opacity="0.85"/>
    </svg>
    <div class="brand stacked-brand">
      <span class="brand-top">MARKETING</span>
      <span class="brand-main">GAZETTOR</span>
    </div>
    <p class="tagline">Essential&nbsp;<span class="hl">Whitepapers</span>&nbsp;for Marketing Professionals</p>
    <div class="cta"><span>CLICK</span><span>HERE</span></div>
  </section>
</main>
</body>
</html>
```